Verdant Loop Advisors, LLC

I am looking for a simple, clear layout with my logo prominent and embossed, on the best quality card stock available. I would like the business name and phone number included on the card as well......I dont want my name anywhere on the card and I would like my logo embossed on the card......something simple with a white back......open to designs as long as they go along with recycling symbols and green type stuff.....The address, website, cell number, fax number, and email are listed below

5374 Tillbury Fenwood Road
Larkmoor, MD 20999

c. 240.555.0143 f. 240.555.0187
e. sales@verdantloopadvisors.example
w. www.verdantloopadvisors.example

Industry/Entity Type

Recycling

```html
<!DOCTYPE html>
<html lang="en">
<head>
<meta charset="utf-8">
<title>Verdant Loop Advisors, LLC — Business Card</title>
<link href="https://fonts.googleapis.com/css2?family=Exo+2:wght@400;800&display=swap" rel="stylesheet">
<style>
  :root {
    --backdrop: #2f2d2c;
    --card-white: #f1f0ec;
    --green-deep: #1f7a3a;
    --green-mid: #2b8a45;
    --green-light: #3f9d55;
    --ink-dark: #2a2622;
    --ink-grey: #6c6a66;
  }
  * { box-sizing: border-box; margin: 0; padding: 0; }
  html, body {
    width: 1200px; height: 901px; overflow: hidden;
    background: var(--backdrop);
    font-family: "Exo 2", Arial, sans-serif;
  }
  .card-sheet {
    position: relative; width: 1200px; height: 901px;
    display: flex; align-items: center; justify-content: center; gap: 60px;
  }
  .card {
    position: relative; width: 525px; height: 300px; overflow: hidden;
    box-shadow: 0 10px 24px rgba(0,0,0,.45);
  }
  .card-front { background: var(--card-white); }
  .card-back { background: var(--green-deep); }

  .brand {
    position: absolute; display: flex; align-items: center; gap: 12px;
    font-weight: 800; text-transform: uppercase; letter-spacing: 1px; line-height: 1.05;
  }
  .brand-mark { width: 30px; height: 30px; flex: none; }
  .card-front .brand { right: 34px; top: 74px; color: var(--ink-dark); font-size: 25px; }
  .card-front .brand-mark { background: var(--green-mid); width: 46px; height: 46px; }
  .card-back .brand { right: 34px; bottom: 34px; color: #ffffff; font-size: 21px; }
  .card-back .brand-mark { background: #ffffff; }

  .contact-list {
    position: absolute; left: 34px; bottom: 34px; list-style: none;
    color: var(--ink-grey); font-size: 13px; line-height: 1.35;
  }
  .contact-item { display: flex; gap: 10px; margin-top: 8px; }
  .contact-icon { width: 12px; height: 12px; flex: none; margin-top: 2px; fill: var(--green-mid); }

  .back-bands { position: absolute; inset: 0; }
</style>
</head>
<body>
<main class="card-sheet">

  <section class="card card-front" aria-label="Card front">
    <div class="brand">
      <span class="brand-mark"></span>
      <span class="brand-name">Verdant Loop<br>Advisors, LLC</span>
    </div>
    <ul class="contact-list">
      <li class="contact-item">
        <svg class="contact-icon" viewBox="0 0 12 12"><path d="M6 0a4 4 0 0 1 4 4c0 3-4 8-4 8S2 7 2 4a4 4 0 0 1 4-4zm0 2.3a1.7 1.7 0 1 0 0 3.4 1.7 1.7 0 0 0 0-3.4z"/></svg>
        <span>5374 Tillbury Fenwood Road<br>Larkmoor, MD 20999</span>
      </li>
      <li class="contact-item">
        <svg class="contact-icon" viewBox="0 0 12 12"><path d="M2.5 0.5l2 2.3-1 1.4a7 7 0 0 0 4.3 4.3l1.4-1 2.3 2-1.3 2A10 10 0 0 1 0.5 1.8z"/></svg>
        <span>c. 240.555.0143<br>f. 240.555.0187</span>
      </li>
      <li class="contact-item">
        <svg class="contact-icon" viewBox="0 0 12 12"><path d="M0 2h12v8H0zM1 3l5 3.5L11 3v-.2H1z"/></svg>
        <span>sales@verdantloopadvisors.example</span>
      </li>
      <li class="contact-item">
        <svg class="contact-icon" viewBox="0 0 12 12"><circle cx="6" cy="6" r="5.5"/><path d="M0.5 6h11M6 0.5c-2.5 3-2.5 8 0 11M6 0.5c2.5 3 2.5 8 0 11" stroke="#f1f0ec" stroke-width=".8" fill="none"/></svg>
        <span>www.verdantloopadvisors.example</span>
      </li>
    </ul>
  </section>

  <section class="card card-back" aria-label="Card back">
    <svg class="back-bands" viewBox="0 0 525 300" preserveAspectRatio="none" aria-hidden="true">
      <polygon points="0,60 300,0 525,0 525,120 0,300" fill="#2b8a45"/>
      <polygon points="0,170 525,20 525,90 0,300" fill="#3f9d55"/>
    </svg>
    <div class="brand">
      <span class="brand-mark"></span>
      <span class="brand-name">Verdant Loop<br>Advisors, LLC</span>
    </div>
  </section>

</main>
</body>
</html>
```